Business Card Design

Just looking for a good designs that looks good with our company logo. I'd like it to be simple and to the point. Just including contact information, our logo, and my name somewhere on the card so future clients know who they're contacting, and a couple services offered. The two images I attached are pictures of our logo. I don't care which color they they are, I just attached both images to give a reference of logo colors depending on the color of the card.
Names: Derek Hallory
Phone: 816-442-7061
Email: greenvalebrush@mailzen.test
Services offered:
Mowing
Fertilization
Aeration
Bed & tree maintenance
and more.
Industry/Entity Type
Business
Contact Information for Business Card
Names: Derek Hallory
Phone: 816-442-7061
Look and feel

```html
<!DOCTYPE html>
<html lang="en">
<head>
<meta charset="utf-8">
<title>Greenvale Brush — Business Card</title>
<link rel="stylesheet" href="https://fonts.googleapis.com/css2?family=Jost:wght@400;500;600&display=swap">
<style>
  :root {
    --backdrop: #d9d9d9;
    --card: #2f3033;
    --ink: #ffffff;
    --accent: #e2553a;
  }
  * { margin: 0; padding: 0; box-sizing: border-box; }
  html, body {
    width: 1200px;
    height: 1199px;
    overflow: hidden;
    background: var(--backdrop);
  }
  .card {
    position: absolute;
    left: 80px;
    top: 295px;
    width: 1040px;
    height: 608px;
    background: var(--card);
    color: var(--ink);
    font-family: "Jost", "Century Gothic", sans-serif;
  }
  .brand {
    position: absolute;
    left: 0;
    right: 0;
    top: 160px;
    display: flex;
    justify-content: center;
    align-items: center;
    gap: 18px;
  }
  .brand-dot {
    width: 34px;
    height: 34px;
    border-radius: 50%;
    background: var(--accent);
  }
  .brand-name {
    font-size: 46px;
    font-weight: 600;
    letter-spacing: 2px;
    text-transform: uppercase;
    color: var(--ink);
  }
  .services {
    position: absolute;
    right: 596px;
    top: 362px;
    list-style: none;
    text-align: right;
    font-size: 24px;
    line-height: 32px;
    font-weight: 400;
  }
  .divider {
    position: absolute;
    left: 501px;
    top: 347px;
    width: 3px;
    height: 184px;
    background: linear-gradient(to bottom, transparent, var(--accent) 30%, var(--accent) 70%, transparent);
  }
  .contact {
    position: absolute;
    left: 562px;
    top: 388px;
  }
  .contact-name {
    font-size: 31px;
    font-weight: 500;
    letter-spacing: 0.5px;
    margin-bottom: 22px;
  }
  .contact-line {
    font-size: 21px;
    line-height: 29px;
    font-weight: 400;
  }
</style>
</head>
<body>
  <section class="card">
    <div class="brand">
      <span class="brand-dot"></span>
      <span class="brand-name">Greenvale Brush</span>
    </div>

    <ul class="services">
      <li>Mowing</li>
      <li>Fertilization</li>
      <li>Aeration</li>
      <li>Bed &amp; tree maintenance</li>
      <li>and more</li>
    </ul>

    <div class="divider"></div>

    <div class="contact">
      <p class="contact-name">Derek Hallory</p>
      <p class="contact-line">816-442-7061</p>
      <p class="contact-line">greenvalebrush@mailzen.test</p>
    </div>
  </section>
</body>
</html>
```